Plumbing & Heating company

A leaflet containing -

Company name - Brackenfold Plumbing Solutions
logo
Mobile number - 07700 914226
Landline - 01632 870512
Email - Info@brackenfoldplumbing.example.co.uk
website - Brackenfold-plumbing.example.co.uk
Social media logos - pixgram, Chatterly

services we offer

- Boiler replacements (free quote)
- General plumbing & heating
- Tap replacements
- 1st & 2nd
- New builds & Extensions
- Cylinder replcemets

```html
<!DOCTYPE html>
<html lang="en">
<head>
<meta charset="utf-8">
<title>Brackenfold Plumbing Solutions – Leaflet</title>
<link href="https://fonts.googleapis.com/css2?family=Oswald:wght@500;600&family=Open+Sans:wght@400;700&family=Hind:wght@600&display=swap" rel="stylesheet">
<style>
  :root{
    --bg:#d4d4d4;
    --paper:#ffffff;
    --slate:#353a3e;
    --frame:#b9bcbf;
    --blue:#124e91;
    --orange:#ee7526;
    --ink:#1e1e1e;
    --chip:#e6e6e6;
    --amber:#f2a51c;
    --red:#e8363f;
    --sky:#1a9ad6;
    --navy:#1d4ea0;
  }
  *{box-sizing:border-box;margin:0;padding:0}
  html,body{width:697px;height:1200px;overflow:hidden;background:var(--bg)}
  .leaflet{
    position:absolute;left:20px;top:177px;width:878px;height:1129px;
    transform:scale(.748);transform-origin:0 0;background:var(--paper);
    font-family:"Open Sans",sans-serif;color:var(--ink);
  }
  .abs{position:absolute}
  .side-dark{left:488px;top:0;width:390px;height:1095px;background:var(--slate)}
  .band-warm{left:0;top:1095px;width:488px;height:34px;background:linear-gradient(90deg,var(--amber),var(--orange) 50%,var(--red))}
  .band-cool{left:488px;top:1095px;width:390px;height:34px;background:linear-gradient(90deg,var(--navy),var(--sky))}
  .dark-frame{left:488px;top:88px;width:352px;height:983px;border:2px solid var(--frame);border-left:none}

  .brand{left:0;top:60px;width:478px;text-align:center;color:var(--blue);font-family:"Oswald",sans-serif;font-weight:600;line-height:1.05}
  .brand-dot{display:block;width:34px;height:34px;border-radius:50%;background:var(--orange);margin:0 auto 14px}
  .brand-name{font-size:44px;letter-spacing:2px}
  .brand-sub{font-size:25px;letter-spacing:4px}

  .title-blue{left:45px;top:276px;font-family:"Oswald",sans-serif;font-weight:600;font-size:25px;color:var(--blue);white-space:nowrap}
  .rule{left:45px;top:324px;width:379px;height:2px;background:#8e9196}
  .title-orange{left:45px;top:340px;font-family:"Oswald",sans-serif;font-weight:600;font-size:33px;line-height:40px;color:var(--orange);white-space:nowrap}
  .intro{left:45px;top:424px;font-size:20px;line-height:29px;white-space:nowrap}

  .gallery{left:44px;top:502px;width:372px;height:446px;border:2px solid #d9c6cc}
  .shot{width:165px;height:200px}
  .shot-1{left:60px;top:517px;background:linear-gradient(160deg,#cfcfcd,#8b8d8f)}
  .shot-2{left:239px;top:517px;width:161px;background:linear-gradient(180deg,#c9c6c0,#3b3a3a 60%,#d9d9d9)}
  .shot-3{left:60px;top:732px;background:linear-gradient(180deg,#ebe6dc 45%,#2a2a2a 70%,#e0e0e0)}
  .shot-4{left:239px;top:732px;width:161px;background:linear-gradient(180deg,#eceae6,#b9b3a8 60%,#caa57c)}

  .email{left:0;top:976px;width:468px;text-align:center;font-size:15px;font-weight:700;white-space:nowrap}
  .email svg{vertical-align:-2px;margin-right:6px}
  .web{left:44px;top:1005px;width:334px;height:54px;background:var(--chip)}
  .web svg{position:absolute;left:6px;top:8px}
  .web-url{position:absolute;left:52px;top:8px;font-size:14px;font-weight:700;color:var(--blue);white-space:nowrap;letter-spacing:-.2px}
  .web-note{position:absolute;left:54px;top:31px;font-size:13px;font-weight:700}
  .social{left:384px;top:1005px;width:87px;height:54px;background:var(--chip);font-size:11px;font-weight:700;color:var(--blue);text-align:center;padding-top:9px;line-height:18px}

  .photo{left:456px;top:142px;width:360px;height:425px;background:linear-gradient(90deg,#c9a178,#e3c39c 35%,#2f3744 60%,#283040 80%,#cfae86);box-shadow:-4px 0 0 #cfc6c6}
  .services-title{left:519px;top:605px;font-family:"Oswald",sans-serif;font-weight:600;font-size:25px;color:#fff}
  .services{left:519px;top:646px;list-style:none;font-family:"Hind",sans-serif;font-weight:600;font-size:18px;color:#fff;line-height:27.7px}
  .services li{white-space:nowrap}
  .services li::before{content:"";display:inline-block;width:14px;height:14px;border-radius:50%;background:radial-gradient(circle at 40% 35%,#ffd36a,var(--amber) 55%,#b86a0c);margin-right:12px;vertical-align:-1px}
  .badges{left:518px;top:844px;width:293px;height:114px;background:#e9e9ea;border-radius:6px}
  .badge-a{left:531px;top:877px;width:152px;height:60px;background:#1d2f6b;border:2px solid #fff;outline:1px solid #999}
  .badge-b{left:703px;top:852px;width:96px;height:97px;background:#fff;border:2px solid #2e9e57}
  .phone{left:520px;top:985px;display:flex;align-items:center;gap:12px;font-family:"Oswald",sans-serif;font-weight:600;font-size:36px;color:#fff;white-space:nowrap}
  .mobile{left:574px;top:1035px;font-family:"Oswald",sans-serif;font-weight:500;font-size:18px;color:#fff;white-space:nowrap}
</style>
</head>
<body>
<main class="leaflet">
  <div class="abs side-dark"></div>
  <div class="abs band-warm"></div>
  <div class="abs band-cool"></div>
  <div class="abs dark-frame"></div>

  <header class="abs brand">
    <span class="brand-dot"></span>
    <div class="brand-name">BRACKENFOLD</div>
    <div class="brand-sub">PLUMBING SOLUTIONS</div>
  </header>

  <h2 class="abs title-blue">BRACKENFOLD PLUMBING SOLUTIONS</h2>
  <div class="abs rule"></div>
  <h1 class="abs title-orange">BRACKENFOLD PLUMBING &amp;<br>HEATING CONTRACTOR</h1>
  <p class="abs intro">Based in Hampshire and covering<br>Winchester and the surrounding areas.</p>

  <div class="abs gallery"></div>
  <div class="abs shot shot-1" role="img" aria-label="Finished bathroom with shower enclosure and basin"></div>
  <div class="abs shot shot-2" role="img" aria-label="Utility room with wall boiler, sink and washing machine"></div>
  <div class="abs shot shot-3" role="img" aria-label="Kitchenette with cream cupboards and steel sink"></div>
  <div class="abs shot shot-4" role="img" aria-label="Under-sink water filter installation"></div>

  <p class="abs email"><svg width="16" height="12" viewBox="0 0 16 12"><rect width="16" height="12" fill="#222"/><path d="M0 0l8 6 8-6" stroke="#fff" stroke-width="1.4" fill="none"/></svg>info@brackenfoldplumbing.example.co.uk</p>

  <div class="abs web">
    <svg width="40" height="40" viewBox="0 0 40 40" fill="none" stroke="#222" stroke-width="2"><circle cx="20" cy="20" r="18"/><ellipse cx="20" cy="20" rx="8" ry="18"/><path d="M2 20h36M5 11h30M5 29h30"/></svg>
    <span class="web-url">Brackenfold-plumbing.example.co.uk</span>
    <span class="web-note">Visit our website</span>
  </div>
  <div class="abs social">Chatterly<br>pixgram</div>

  <div class="abs photo" role="img" aria-label="Engineer in branded gilet fitting copper pipework and a heating manifold"></div>

  <h3 class="abs services-title">SERVICES WE OFFER</h3>
  <ul class="abs services">
    <li>Boiler replacements (Free Quote)</li>
    <li>General plumbing &amp; heating</li>
    <li>Tap replacements</li>
    <li>1st &amp; 2nd</li>
    <li>New builds &amp; Extensions</li>
    <li>Cylinder replcemets</li>
  </ul>

  <div class="abs badges"></div>
  <div class="abs badge-a" role="img" aria-label="Gas safety registration badge"></div>
  <div class="abs badge-b" role="img" aria-label="Approved boiler installer badge"></div>

  <div class="abs phone">
    <svg width="42" height="42" viewBox="0 0 42 42"><circle cx="21" cy="21" r="21" fill="var(--orange)"/><path d="M11 18c0-4 5-6 10-6s10 2 10 6l-4 1-1-3c-3-1-7-1-10 0l-1 3zM14 22h14l2 8H12z" fill="#fff"/><circle cx="21" cy="26" r="2.5" fill="var(--orange)"/></svg>
    <span>01632 870512</span>
  </div>
  <p class="abs mobile">Mobile: 07700 914226</p>
</main>
</body>
</html>
```